Hello Creative Minds!
Our business is after a elegant and classy flyer that draws attention!
The business is Tallow Brook - Lawn Rejuvenation Services. We provide services that maintain a healthy and vibrant green lawn through the tough Australian seasons. The products we use limits the water needed to keep grass green to a minimum - practically none at all! This not only helps the home owner or home seller but the environment by limiting the use of water that is needed to create a green lawn. The products we use are made from natural ingredients that are and pet friendly.
This fly will be our introductory offer to the market. Below are the required points that need to be on the flyer. Attached is the business logo, before & after pictures and 1 example of the LAYOUT not DESIGN of what the flyer should be laid out like or similar to. Feel free to use different 'Lawn Mower' pictures.
All the best; if you need any questions answered please feel free to message.
REQUIRED POINTS (Please re-phrase were possible);
*Instantly restores the natural green colour of grass – year round
*Lasts for up to 3 months
*Substantially reduces watering needs
*Pet friendly
*Stays green during droughts and water restrictions
*UV fade resistant
*Won’t bleed, run, or stain once absorbed into the grass
*Safe for the environment, pets and people
*Works in extreme heat, cold and frost
*Organic and natural – no harmful chemicals
*Reduces the amount of fertilizer
and water used on lawns
*Kerb appeal is essential for getting your property sold for the highest price possible
SERVICES & PRICING
Lawn maintenance (cut & trim) starting from $60
Lawn rejuvenation starting from $80 (Only $27 a month for 3 months)*
Package deal starting from $120
Introductory offer: 25% off all services. Refer a friend, when they book you receive another 25% off your next service.
LOCATIONS
Nowra to Sydney
CONTACT NUMBER
Will be posted with the winner - please leave an area for this.
SOCIAL MEDIA
Please add Facebook and Instagram logo's
Updates
Competition has finished, thank you to all that have participated! I will review and comment on the flyers that need assistance. All the best with future designs!
Target Market(s)
home owners, home sellers, property developers, real estates and nursing homes and government housing.
Industry/Entity Type
Lawn Care
Look and feel

```html
<!DOCTYPE html>
<html lang="en">
<head>
<meta charset="utf-8">
<title>Tallow Brook - Lawn Rejuvenation Services</title>
<link href="https://fonts.googleapis.com/css2?family=Poppins:wght@400;500;600;700&family=Oswald:wght@500&display=swap" rel="stylesheet">
<style>
  :root {
    --page: #e9e9e7;
    --slate: #34363d;
    --slate-deep: #24262b;
    --green: #1f9a1f;
    --green-bright: #36b52c;
    --green-deep: #0d6d12;
    --mist: #efefef;
    --ink: #5a5a5a;
    --white: #ffffff;
  }
  * { margin: 0; padding: 0; box-sizing: border-box; }
  html, body { width: 1113px; height: 1200px; overflow: hidden; background: var(--page); }
  body { position: relative; font-family: "Poppins", sans-serif; }

  .flyer {
    position: absolute; left: 156px; top: 40px; width: 800px; height: 1120px;
    overflow: hidden; background: var(--mist);
    box-shadow: 0 4px 14px rgba(0,0,0,.25);
  }
  .lawn-photo {
    position: absolute; left: 0; top: 0; width: 800px; height: 820px;
    background:
      radial-gradient(ellipse at 50% 30%, var(--green-bright) 0%, var(--green) 45%, var(--green-deep) 75%, transparent 100%),
      linear-gradient(180deg, var(--green) 0%, var(--green) 68%, var(--mist) 84%);
    -webkit-mask-image: linear-gradient(180deg, #000 0%, #000 70%, transparent 88%);
    mask-image: linear-gradient(180deg, #000 0%, #000 70%, transparent 88%);
  }
  .mower-photo {
    position: absolute; left: 540px; top: 20px; width: 240px; height: 215px;
    background: radial-gradient(ellipse at 55% 55%, #3c4a2e 0%, #2a4a22 40%, rgba(31,120,31,0) 75%);
  }
  .header-band { position: absolute; left: 0; top: 0; width: 800px; height: 260px; }

  .brand { position: absolute; left: 30px; top: 60px; width: 340px; text-align: center; color: var(--white); }
  .brand-name { font-size: 44px; font-weight: 500; line-height: 1.1; }
  .brand-tag { font-size: 11px; letter-spacing: 3px; margin-top: 6px; }

  .section { position: absolute; left: 0; width: 800px; text-align: center; color: var(--white); }
  .section-title {
    display: flex; align-items: center; justify-content: center; gap: 8px;
    font-size: 31px; font-weight: 600; text-shadow: 0 1px 3px rgba(0,0,0,.35);
  }
  .section-title::before, .section-title::after { content: ""; width: 80px; height: 2px; background: var(--white); }
  .pricing { top: 262px; }
  .pricing .line { font-size: 20px; line-height: 29px; }
  .pricing .price { font-size: 27px; font-weight: 700; }
  .offer { top: 420px; }
  .offer .line { font-size: 23px; line-height: 30px; font-weight: 500; }
  .offer b { font-weight: 700; }

  .benefits { position: absolute; left: 40px; top: 652px; list-style: none; color: var(--ink); }
  .benefits li { position: relative; padding-left: 25px; font-size: 16.3px; line-height: 26.2px; }
  .benefits li svg { position: absolute; left: 0; top: 6px; }
  .benefits .wrap { display: block; }

  .result-photo {
    position: absolute; left: 595px; width: 165px; height: 165px; border-radius: 50%;
    border: 6px solid var(--green);
  }
  .result-before-after { top: 645px; background: linear-gradient(90deg, #b39a6b 0%, #a88e5e 48%, #4f7a35 52%, #3f6c2a 100%); }
  .result-home { top: 822px; background: linear-gradient(180deg, #c8c8c6 0%, #8e9a7a 35%, #5c6462 60%, #6f8d45 100%); }

  .grass-edge {
    position: absolute; left: 0; top: 1012px; width: 800px; height: 42px;
    background: linear-gradient(180deg, rgba(54,181,44,0) 0%, var(--green-bright) 70%, var(--green) 100%);
  }
  .footer {
    position: absolute; left: 0; top: 1052px; width: 800px; height: 68px;
    background: var(--green-deep);
    display: flex; align-items: center; padding: 0 22px;
    font-family: "Oswald", sans-serif; font-weight: 500; font-size: 28px; color: var(--white); letter-spacing: .5px;
  }
  .footer .location { width: 370px; }
  .footer .phone { flex: 1; }
  .social { display: flex; gap: 8px; }
  .social span { width: 28px; height: 28px; border-radius: 50%; background: var(--white); }
</style>
</head>
<body>
<main class="flyer">
  <div class="lawn-photo" role="img" aria-label="Photo of a lush green mowed lawn"></div>
  <div class="mower-photo" role="img" aria-label="Photo of a lawn mower on grass"></div>

  <svg class="header-band" viewBox="0 0 800 260" aria-hidden="true">
    <path d="M0 0 H800 V6 C700 20 620 60 520 115 C420 170 300 200 0 205 Z" fill="var(--slate)"/>
    <path d="M0 205 C300 200 420 170 520 115 C620 60 700 20 800 6 L800 14 C700 30 630 70 530 125 C430 180 310 212 0 218 Z" fill="var(--green-bright)"/>
  </svg>

  <div class="brand">
    <div class="brand-name">Tallow Brook</div>
    <div class="brand-tag">LAWN REJUVENATION SERVICES</div>
  </div>

  <section class="section pricing">
    <h2 class="section-title">SERVICES &amp; PRICING</h2>
    <p class="line">Lawn maintenance (cut &amp; trim) starting from <span class="price">$60</span></p>
    <p class="line">Lawn rejuvenation starting from <span class="price">$80</span> (Only $27 a month for 3 months)*</p>
    <p class="line">Package deal starting from <span class="price">$120</span></p>
  </section>

  <section class="section offer">
    <h2 class="section-title">INTRODUCTORY OFFER</h2>
    <p class="line"><b>25% off</b> all services.</p>
    <p class="line">Refer a friend, when they book you receive another</p>
    <p class="line"><b>25% off</b> your next service.</p>
  </section>

  <svg width="0" height="0" style="position:absolute">
    <symbol id="tick" viewBox="0 0 14 14"><path d="M1.5 7.5 L5.5 11.5 L12.5 2.5" fill="none" stroke="#1f9a1f" stroke-width="2.6" stroke-linecap="round" stroke-linejoin="round"/></symbol>
  </svg>
  <ul class="benefits">
    <li><svg width="14" height="14"><use href="#tick"/></svg>Instantly restores the natural green colour of grass – year round</li>
    <li><svg width="14" height="14"><use href="#tick"/></svg>Lasts for up to 3 months</li>
    <li><svg width="14" height="14"><use href="#tick"/></svg>Substantially reduces watering needs</li>
    <li><svg width="14" height="14"><use href="#tick"/></svg>Pet friendly</li>
    <li><svg width="14" height="14"><use href="#tick"/></svg>Stays green during droughts and water restrictions</li>
    <li><svg width="14" height="14"><use href="#tick"/></svg>UV fade resistant</li>
    <li><svg width="14" height="14"><use href="#tick"/></svg>Won’t bleed, run, or stain once absorbed into the grass</li>
    <li><svg width="14" height="14"><use href="#tick"/></svg>Safe for the environment, pets and people</li>
    <li><svg width="14" height="14"><use href="#tick"/></svg>Works in extreme heat, cold and frost</li>
    <li><svg width="14" height="14"><use href="#tick"/></svg>Organic and natural – no harmful chemicals</li>
    <li><svg width="14" height="14"><use href="#tick"/></svg>Reduces the amount of fertilizer and water used on lawns</li>
    <li><svg width="14" height="14"><use href="#tick"/></svg>Kerb appeal is essential for getting your property<span class="wrap">sold for the highest price possible</span></li>
  </ul>

  <div class="result-photo result-before-after" role="img" aria-label="Before and after photo of dry brown grass beside green rejuvenated grass"></div>
  <div class="result-photo result-home" role="img" aria-label="Photo of a house front yard with a green lawn"></div>

  <div class="grass-edge" role="img" aria-label="Grass blades border"></div>
  <footer class="footer">
    <span class="location">LOCATIONS : NOWRA TO SYDNEY</span>
    <span class="phone">CALL US : 555-014-2276</span>
    <span class="social" aria-label="Social media"><span></span><span></span></span>
  </footer>
</main>
</body>
</html>
```